Wageline Associates Business Card Design

We need a business card designed around our new logo. The business card should be modern in design & should communicate success, confidence, power, sophistication. The target market is young business professionals. This is for a human resource & payroll outsourcing business.

```html
<!DOCTYPE html>
<html lang="en">
<head>
<meta charset="utf-8">
<title>Wageline Associates Business Card</title>
<link rel="stylesheet" href="https://fonts.googleapis.com/css2?family=Crimson+Text:wght@400;600&display=swap">
<style>
  :root {
    --backdrop: #2b2b2b;
    --card: #1f1f1f;
    --accent: #e3161f;
    --ink: #ffffff;
    --ink-soft: #d9d9d9;
    --emboss: #3a3a3a;
  }
  * { margin: 0; padding: 0; box-sizing: border-box; }
  html, body {
    width: 1200px; height: 1200px; overflow: hidden;
    background: var(--backdrop);
    font-family: "Crimson Text", Georgia, serif;
  }
  .stage {
    width: 1200px; height: 1200px;
    display: flex; flex-direction: column; align-items: center; justify-content: center;
    gap: 40px;
  }
  .card {
    position: relative;
    width: 880px; height: 503px;
    background: var(--card);
    border-bottom: 7px solid var(--accent);
    box-shadow: 0 18px 40px rgba(0,0,0,0.45);
  }
  /* Front */
  .card-front .brand {
    position: absolute; left: 70px; top: 250px; width: 340px;
    display: flex; align-items: center; gap: 16px;
    color: var(--ink); font-weight: 600; font-size: 50px; line-height: 1;
  }
  .brand-dot {
    width: 20px; height: 20px; border-radius: 50%; background: var(--accent); flex: none;
  }
  .brand-name { display: block; }
  .divider {
    position: absolute; left: 470px; top: 70px; width: 2px; height: 360px;
    background: var(--accent);
  }
  .contact {
    position: absolute; left: 510px; top: 90px; right: 30px; color: var(--ink-soft);
  }
  .contact-name {
    color: var(--accent); font-size: 34px; font-weight: 400; letter-spacing: 1px;
    text-transform: uppercase; line-height: 1;
  }
  .contact-role { font-size: 20px; margin-top: 8px; }
  .contact-address { font-size: 20px; margin-top: 24px; line-height: 1.4; }
  .contact-list { list-style: none; margin-top: 22px; font-size: 20px; line-height: 1.55; }
  .contact-list li { display: flex; align-items: center; gap: 12px; white-space: nowrap; }
  .contact-list svg { width: 16px; height: 16px; flex: none; }
  /* Back */
  .card-back .brand-large {
    position: absolute; left: 0; right: 0; top: 170px; text-align: center;
    color: var(--emboss); font-weight: 600; font-size: 70px; line-height: 1;
  }
  .web {
    position: absolute; left: 0; right: 0; bottom: 90px; text-align: center;
    color: var(--ink); font-size: 24px; letter-spacing: 2px;
  }
  .web-name { color: var(--accent); }
</style>
</head>
<body>
<main class="stage">
  <section class="card card-front">
    <div class="brand"><span class="brand-dot"></span><span class="brand-name">Wageline<br>Associates</span></div>
    <div class="divider"></div>
    <div class="contact">
      <h1 class="contact-name">Jordan Reyes</h1>
      <p class="contact-role">Director</p>
      <p class="contact-address">4810 Harbor View Drive #210<br>Tampa, FL 33609</p>
      <ul class="contact-list">
        <li><svg viewBox="0 0 16 16"><path fill="#e3161f" d="M3.5 1.5l2.5 2.8-1.3 1.6c.9 2 2.5 3.5 4.4 4.4l1.6-1.3 2.8 2.5-1.4 2.1C7.5 13.5 2.5 8.5 1.4 3z"/></svg>+31 (0)20 555 01 47</li>
        <li><svg viewBox="0 0 16 16"><rect x="1.5" y="3.5" width="13" height="9" fill="none" stroke="#e3161f" stroke-width="1.6"/><path d="M1.5 3.5L8 9l6.5-5.5" fill="none" stroke="#e3161f" stroke-width="1.6"/></svg>info@wagelineassociates.com</li>
        <li><svg viewBox="0 0 16 16"><circle cx="8" cy="8" r="6.5" fill="none" stroke="#e3161f" stroke-width="1.5"/><ellipse cx="8" cy="8" rx="2.8" ry="6.5" fill="none" stroke="#e3161f" stroke-width="1.2"/><path d="M1.5 8h13" stroke="#e3161f" stroke-width="1.2"/></svg>www.wagelineassociates.com</li>
      </ul>
    </div>
  </section>
  <section class="card card-back">
    <div class="brand-large">Wageline Associates</div>
    <p class="web">www.<span class="web-name">wagelineassociates</span>.com</p>
  </section>
</main>
</body>
</html>
```